Vireo Halden Business Cards

Vireo Halden Luxury Brand Collection is a global representation business focusing on high end luxury. We need business cards to epitomize our global, luxury delivery model.

Target Market(s)

Global Representation in the hospitality industry

Industry/Entity Type

Hospitality

Contact Information for Business Card

name
title
email: first.last@vh-kmt.com
web: www.vh-kmt.com
mobile:

Requirements
Must have
• double sided design
• incorporate logo colours
• have logo prominent
Should not have
• no designs not incorporating logo colours.

```html
<!DOCTYPE html>
<html lang="en">
<head>
<meta charset="utf-8">
<title>Vireo Halden Business Cards</title>
<link href="https://fonts.googleapis.com/css2?family=EB+Garamond:wght@400;600&display=swap" rel="stylesheet">
<style>
  :root {
    --backdrop: #2a2c30;
    --gold-light: #a88d50;
    --gold-dark: #8f7644;
    --ink: #1a1a1a;
    --black-light: #272727;
    --black-dark: #1b1b1b;
    --gold-text: #a58a4f;
  }
  * { margin: 0; padding: 0; box-sizing: border-box; }
  html, body { width: 1200px; height: 900px; overflow: hidden; }
  body {
    background: var(--backdrop);
    font-family: "EB Garamond", Georgia, serif;
    position: relative;
  }
  .card {
    position: absolute;
    top: 307px;
    width: 500px;
    height: 286px;
    overflow: hidden;
    box-shadow: 0 14px 30px rgba(0,0,0,0.45);
  }
  .card--front { left: 70px; background: linear-gradient(to bottom, var(--gold-light) 0 50%, var(--gold-dark) 50% 100%); }
  .card--back { left: 630px; background: linear-gradient(to bottom, var(--black-light) 0 28%, var(--black-dark) 28% 100%); }
  .edge-strip { position: absolute; left: 0; top: 0; bottom: 0; width: 22px; }
  .card--front .edge-strip { background: var(--ink); }
  .card--back .edge-strip { background: var(--gold-light); }

  .front-content {
    position: absolute; inset: 0 0 0 22px;
    display: flex; flex-direction: column; align-items: center;
    color: var(--ink); text-align: center;
    padding-top: 30px;
  }
  .holder-name { font-size: 26px; font-weight: 600; letter-spacing: 1px; text-transform: uppercase; line-height: 1; }
  .holder-title { font-size: 14px; letter-spacing: 1.5px; text-transform: uppercase; margin-top: 4px; }
  .brand-mark { font-size: 30px; font-weight: 600; margin: 30px 0 26px; line-height: 1; }
  .contact-line { font-size: 15px; line-height: 1.5; }
  .contact-line .divider { margin: 0 8px; }

  .back-content {
    position: absolute; inset: 0 0 0 22px;
    display: flex; align-items: center; justify-content: center;
  }
  .brand-mark--large { font-size: 52px; font-weight: 600; color: var(--gold-text); margin: 0; }
</style>
</head>
<body>
  <section class="card card--front" aria-label="Business card front">
    <div class="edge-strip"></div>
    <div class="front-content">
      <p class="holder-name">Marlow Renick</p>
      <p class="holder-title">Director</p>
      <p class="brand-mark">Vireo Halden</p>
      <p class="contact-line">Mob: 014 482 60317</p>
      <p class="contact-line">first.last@vh-kmt.com<span class="divider">|</span>www.vh-kmt.com</p>
    </div>
  </section>

  <section class="card card--back" aria-label="Business card back">
    <div class="edge-strip"></div>
    <div class="back-content">
      <p class="brand-mark brand-mark--large">Vireo Halden</p>
    </div>
  </section>
</body>
</html>
```